11 x 11 Flyer Design for Social Media - Reverse Mortgages

62 or older?

A Reverse Mortgage
could be
Your Road to Financial Freedom

* No Monthly Payments
* No Income Requirements
* No Credit Score Requirements
* No Loss of Ownership

Receive cash by lump sum, monthly installments or a line of credit!!

Call us today for a Free Consultation!!
(800) 471-2965

Bluegate Financial Services, Inc.
NMLS #318760
www.bluegatehome.com

```html
<!DOCTYPE html>
<html lang="en">
<head>
<meta charset="utf-8">
<title>Reverse Mortgage Flyer – Bluegate Financial Services</title>
<link href="https://fonts.googleapis.com/css2?family=Roboto:wght@400;500;700;900&display=swap" rel="stylesheet">
<style>
  :root {
    --navy: #0e4677;
    --green: #3fa68a;
    --white: #ffffff;
    --ring: #ece4df;
    --photo-a: #9fb9c9;
    --photo-b: #3b3f4a;
  }
  * { margin: 0; padding: 0; box-sizing: border-box; }
  html, body { width: 1200px; height: 1200px; overflow: hidden; }
  body { font-family: "Roboto", Arial, sans-serif; background: var(--navy); color: var(--white); }
  .flyer { position: relative; width: 1200px; height: 1200px; background: var(--navy); overflow: hidden; }
  .corner-blob { position: absolute; left: 0; top: 0; width: 1200px; height: 1200px; }
  .hero-photo {
    position: absolute; left: 828px; top: -26px; width: 400px; height: 400px;
    border-radius: 50%; border: 11px solid var(--ring);
    background: radial-gradient(circle at 40% 55%, #c9b7a8 0%, var(--photo-a) 45%, var(--photo-b) 100%);
  }
  .age-question {
    position: absolute; left: 198px; top: 112px;
    font-size: 94px; font-weight: 700; color: var(--green); letter-spacing: -1px; line-height: 1;
  }
  .headline {
    position: absolute; left: 200px; top: 214px;
    font-size: 58px; font-weight: 400; line-height: 72px; letter-spacing: -0.3px;
  }
  .payout-options {
    position: absolute; left: 200px; top: 433px;
    font-size: 23px; line-height: 36px; font-weight: 400;
  }
  .benefits { position: absolute; left: 48px; top: 645px; list-style: none; }
  .benefits li {
    display: flex; align-items: center; height: 72px;
    font-size: 40px; font-weight: 400;
  }
  .benefits svg { width: 38px; height: 38px; margin-right: 20px; flex: none; }
  .call-tab {
    position: absolute; left: 895px; top: 697px; width: 142px; height: 70px;
    background: var(--green); border-radius: 8px 8px 0 0;
    display: flex; justify-content: center; align-items: center; padding-bottom: 8px;
  }
  .call-tab svg { width: 52px; height: 52px; }
  .call-box {
    position: absolute; left: 686px; top: 758px; width: 499px; height: 136px;
    background: var(--green); border-radius: 8px; text-align: center;
    box-shadow: 0 4px 0 rgba(0,0,0,0.15);
  }
  .call-prompt { margin-top: 18px; font-size: 24px; font-weight: 700; }
  .call-number { margin-top: 6px; font-size: 42px; font-weight: 700; letter-spacing: 0.5px; }
  .company-name { position: absolute; left: 53px; top: 1108px; font-size: 37px; font-weight: 700; }
  .license { position: absolute; left: 53px; top: 1154px; font-size: 24px; font-weight: 400; }
  .website { position: absolute; right: 26px; top: 1146px; font-size: 28px; font-weight: 500; }
</style>
</head>
<body>
<main class="flyer">
  <svg class="corner-blob" viewBox="0 0 792 792" aria-hidden="true">
    <path d="M0,0 H140 C100,35 58,80 72,160 C86,240 120,310 0,350 Z" fill="#3fa68a"/>
  </svg>

  <div class="hero-photo" role="img" aria-label="Photo of a smiling senior couple taking a selfie by the sea"></div>

  <h1 class="age-question">62 or older?</h1>
  <h2 class="headline">A Reverse Mortgage<br>could be Your Road to<br>Financial Freedom</h2>
  <p class="payout-options">Receive cash by lump sum,<br>monthly installments or a line of credit!!</p>

  <ul class="benefits">
    <li><svg viewBox="0 0 24 24"><circle cx="12" cy="12" r="12" fill="#3fa68a"/><path d="M6.5 12.5l3.6 3.5 7.4-7.6" fill="none" stroke="#0e4677" stroke-width="2.8" stroke-linecap="round" stroke-linejoin="round"/></svg>No Monthly Payments</li>
    <li><svg viewBox="0 0 24 24"><circle cx="12" cy="12" r="12" fill="#3fa68a"/><path d="M6.5 12.5l3.6 3.5 7.4-7.6" fill="none" stroke="#0e4677" stroke-width="2.8" stroke-linecap="round" stroke-linejoin="round"/></svg>No Income Requirements</li>
    <li><svg viewBox="0 0 24 24"><circle cx="12" cy="12" r="12" fill="#3fa68a"/><path d="M6.5 12.5l3.6 3.5 7.4-7.6" fill="none" stroke="#0e4677" stroke-width="2.8" stroke-linecap="round" stroke-linejoin="round"/></svg>No Credit Score Requirements</li>
    <li><svg viewBox="0 0 24 24"><circle cx="12" cy="12" r="12" fill="#3fa68a"/><path d="M6.5 12.5l3.6 3.5 7.4-7.6" fill="none" stroke="#0e4677" stroke-width="2.8" stroke-linecap="round" stroke-linejoin="round"/></svg>No Loss of Ownership</li>
  </ul>

  <div class="call-tab">
    <svg viewBox="0 0 24 24" aria-hidden="true"><path d="M6.6 3.5l2.6 3.4c.4.5.3 1.2-.1 1.6L7.6 10c1.2 2.6 3.7 5.1 6.4 6.4l1.5-1.5c.4-.4 1.1-.5 1.6-.1l3.4 2.6c.5.4.6 1.1.2 1.6l-1.6 1.9c-.6.7-1.6 1-2.5.7C10 19.6 4.4 14 2.4 7.4c-.3-.9 0-1.9.7-2.5l1.9-1.6c.5-.4 1.2-.3 1.6.2z" fill="none" stroke="#ffffff" stroke-width="1.5" stroke-linejoin="round"/></svg>
  </div>
  <div class="call-box">
    <p class="call-prompt">Call us today for a Free Consultation!!</p>
    <p class="call-number">(800) 471-2965</p>
  </div>

  <p class="company-name">Bluegate Financial Services, Inc.</p>
  <p class="license">NMLS #318760</p>
  <p class="website">www.bluegatehome.com</p>
</main>
</body>
</html>
```